Lukas Brandstetter, systemic consultant.

Minimalism as a lifestyle means: conscious renunciation to make room for the essentials. My homepage should present itself easily and clearly. Just design in the colors of the logo, thanks. Insert my personal photos very discreetly. Clear headings that convey seriousness, clarity and confidence. As a systemic consultant, I usually coach clients virtually using video chat (zoom). Clear solutions and support are my core competence. My homepage should be sober and yet inviting and arouse curiosity. The focus is my consulting skills and my life experience! My services are honest, human and trustworthy. My homepage is not complicated, playful and chaotic. It is clear and clearly structured. Less is more!! My homepage should also have a podcast.

Target Market(s)

Highly sensitive people between 20-60, artists, actors, athletes, managers...

Industry/Entity Type

Coaching-Leading

Font styles to use
Serif

Requirements
Must have
• Clarity, openness, digital, structure, simple, seriousness, good feeling!!
Nice to have
• Big photos and pictures. Colors from the logo, only 3 pages hp would be optimal, a simple-simple homepage!
Should not have
• Colourful, complicated, nested, playful.

```html
<!DOCTYPE html>
<html lang="en">
<head>
<meta charset="utf-8">
<title>Lukas Brandstetter – Systemic Consultant</title>
<link href="https://fonts.googleapis.com/css2?family=Merriweather:wght@300;400;700;900&display=swap" rel="stylesheet">
<style>
:root{
  --red:#a50021;
  --black:#000;
  --white:#fff;
  --ink:#1b1b1b;
  --muted:#4a4a4a;
  --grey:#d9d9db;
  --ring:#b5b5b5;
  --pale:#eef2fb;
  --pink:#f6c6d0;
  --star:#f3b51b;
}
*{margin:0;padding:0;box-sizing:border-box}
html,body{width:1200px;height:4409px;overflow:hidden}
body{position:relative;background:var(--white);font-family:"Merriweather",Georgia,serif;color:var(--ink)}
.abs{position:absolute}

/* Header / hero */
.hero{left:0;top:0;width:1200px;height:673px;background:var(--black);border-bottom-right-radius:150px;overflow:hidden}
.hero-backdrop{right:0;top:90px;width:560px;height:583px;background:radial-gradient(ellipse at 55% 50%,#2a2a2a 0%,#141414 55%,#000 80%)}
.brand{display:flex;align-items:center;gap:8px;color:var(--white)}
.brand-dot{width:22px;height:22px;border-radius:50%;background:var(--red);flex:none}
.brand-name{font-size:14px;letter-spacing:2.4px;text-transform:uppercase;line-height:1;white-space:nowrap}
.brand-tag{font-size:6px;letter-spacing:2px;color:var(--red);text-transform:uppercase;margin-top:3px}
.nav{top:29px;left:390px;font-size:15px;color:var(--white)}
.nav a{color:inherit;text-decoration:none;position:absolute;white-space:nowrap}
.nav a.active{color:var(--red)}
.phone-btn{left:919px;top:20px;width:170px;height:38px;background:var(--red);border-radius:6px 14px 6px 6px;color:var(--white);font-size:15px;display:flex;align-items:center;justify-content:center;gap:8px}
.portrait-ring{left:90px;top:141px;width:430px;height:430px;border-radius:50%;border:9px solid var(--red);background:var(--white);overflow:hidden}
.portrait{left:70px;top:20px;width:272px;height:400px;border-radius:136px 136px 0 0;background:linear-gradient(180deg,#c79c84 0%,#7d5f52 22%,#1e1e22 45%,#111 100%)}
.hero-title{left:570px;top:228px;font-size:58px;font-weight:900;line-height:62px;color:var(--white);letter-spacing:.5px;white-space:nowrap}
.hero-title em{font-style:normal;color:var(--red)}
.btn{background:var(--red);color:var(--white);font-size:22px;display:flex;align-items:center;justify-content:center;border-radius:0 14px 0 0}
.hero-btn{left:573px;top:383px;width:148px;height:50px}
.scroll-marks{left:1141px;top:228px;width:3px}
.scroll-marks span{display:block;width:3px;height:18px;background:var(--white);margin-bottom:22px}
.scroll-marks span.on{background:var(--red);height:24px}

/* Headings */
.section-title{width:1200px;left:0;text-align:center;font-size:36px;font-weight:700;color:var(--ink)}
.rule{height:2px;background:var(--red)}

/* About */
.about-text{left:216px;top:836px;width:768px;text-align:center;font-size:17.5px;line-height:29px;color:var(--muted);font-weight:300}
.about-text p+p{margin-top:29px}
.about-btn{left:527px;top:1113px;width:146px;height:49px}

/* Services */
.services{left:0;top:1263px;width:1200px;height:603px;background:var(--red);border-top-left-radius:200px}
.services .section-title{color:var(--white)}
.svc{width:320px;height:320px}
.svc-body{left:37px;top:37px;width:246px;height:246px;border-radius:50%;display:flex;flex-direction:column;align-items:center;justify-content:center;text-align:center;padding:0 34px}
.svc-body h3{font-size:21px;font-weight:700;margin-bottom:20px}
.svc-body p{font-size:17.5px;line-height:29px;font-weight:300}
.svc-light .svc-body{background:var(--pale);color:#111}
.svc-light .svc-body p{color:#333}
.svc-dark .svc-body{background:var(--black);color:var(--white)}

/* Testimonials */
.quote-badge{left:570px;top:2050px;width:64px;height:64px;border-radius:50%;background:var(--red)}
.t-name{left:0;width:1200px;top:2128px;text-align:center;font-size:26px;font-weight:700}
.t-name .stars{color:var(--star);font-size:18px;margin-left:10px;letter-spacing:1px}
.t-text{left:266px;width:675px;top:2178px;text-align:center;font-size:17.5px;line-height:28px;color:var(--muted);font-weight:300}
.t-thanks{left:0;width:1200px;top:2312px;text-align:center;font-size:18px;color:#222}
.t-thanks b{font-weight:700}
.t-side{font-size:17.5px;line-height:28px;color:#b9b9b9;font-weight:300;text-align:center;width:320px}
.t-side-name{font-size:26px;color:#b9b9b9}
.dots{left:548px;top:2390px;display:flex;gap:20px}
.dots span{width:17px;height:2px;background:#333}
.dots span.on{width:34px;background:var(--red)}

/* Video */
.video-band{left:0;top:2476px;width:1200px;height:626px;background:var(--grey);border-bottom-left-radius:210px}
.video-frame{left:115px;top:2559px;width:976px;height:454px;border:5px solid var(--black);border-top-color:var(--red);border-right-color:var(--red)}
.video-still{left:0;top:0;width:100%;height:100%;background:linear-gradient(100deg,#efe5da 0%,#b8a596 30%,#8d7a6d 52%,#4b4a58 70%,#d8d2cb 100%)}
.play{left:452px;top:192px;width:62px;height:62px}
.video-brand{left:317px;top:393px;width:334px;height:46px;background:var(--black);display:flex;align-items:center;justify-content:center}

/* News */
.card{width:308px;height:433px;background:var(--white);box-shadow:0 3px 10px rgba(0,0,0,.18);top:3299px}
.card-img{left:0;top:0;width:308px;height:202px}
.card-stars{left:14px;top:220px;font-size:17px;color:var(--star);letter-spacing:6px}
.card-stars span{color:#444;letter-spacing:0;font-size:15px;margin-left:4px}
.card h3{position:absolute;left:14px;top:251px;font-size:20.5px;font-weight:700;white-space:nowrap}
.card-date{left:14px;top:284px;font-size:8px;color:var(--red)}
.card-text{left:14px;top:302px;width:284px;font-size:17px;line-height:26px;color:#333;font-weight:300}
.card-foot{left:0;top:395px;width:308px;height:38px;background:var(--pink);display:flex;align-items:center;padding-left:14px;gap:8px;font-size:17px;font-weight:700}
.avatar{width:22px;height:22px;border-radius:50%;background:#9a7a66}
.news-btn{left:529px;top:3797px;width:146px;height:50px}

/* Footer */
.footer{left:0;top:3929px;width:1200px;height:480px;background:var(--black);border-top-left-radius:210px;color:var(--white)}
.f-about{left:115px;top:152px;width:211px;font-size:15.5px;line-height:27.5px;color:#e8e8e8;text-align:justify;font-weight:300}
.f-head{top:108px;font-size:19.5px;font-weight:700;text-transform:uppercase;letter-spacing:.3px}
.f-list{font-size:15px;line-height:19px;color:#e8e8e8;font-weight:300}
.f-item{display:flex;gap:8px;align-items:flex-start;position:absolute;white-space:nowrap}
.f-item svg{flex:none;margin-top:2px}
.f-link{position:absolute;font-size:15.5px;color:#e8e8e8;font-weight:300;white-space:nowrap}
.social{width:26px;height:26px;border-radius:50%;background:var(--red)}
.news-input{left:878px;top:151px;width:214px;height:35px;background:var(--white);color:#555;font-size:11px;display:flex;align-items:center;padding-left:16px}
.news-submit{left:878px;top:213px;width:214px;height:40px;background:var(--red);color:var(--white);font-size:17px;font-weight:700;display:flex;align-items:center;justify-content:center}
.f-rule{left:115px;top:393px;width:977px;height:1px;background:#777}
.copyright{left:0;width:1200px;top:425px;text-align:center;font-size:15px;color:#e8e8e8}
</style>
</head>
<body>

<!-- Hero -->
<header class="abs hero">
  <div class="abs hero-backdrop" role="img" aria-label="Faint dark photograph of a tiger"></div>
  <div class="abs brand" style="left:108px;top:26px">
    <span class="brand-dot"></span>
    <div><div class="brand-name">Lukas Brandstetter</div><div class="brand-tag">Systemic Consulting</div></div>
  </div>
  <nav class="abs nav">
    <a class="active" style="left:0">Home</a>
    <a style="left:83px">About Me</a>
    <a style="left:193px">Services</a>
    <a style="left:294px">Testimonials</a>
    <a style="left:432px">Contact</a>
  </nav>
  <div class="abs phone-btn">
    <svg width="14" height="14" viewBox="0 0 24 24" fill="none" stroke="#fff" stroke-width="2.4"><path d="M22 16.9v3a2 2 0 0 1-2.2 2 19.8 19.8 0 0 1-8.6-3.1 19.5 19.5 0 0 1-6-6A19.8 19.8 0 0 1 2.1 4.2 2 2 0 0 1 4.1 2h3a2 2 0 0 1 2 1.7c.1 1 .4 1.9.7 2.8a2 2 0 0 1-.5 2.1L8 9.9a16 16 0 0 0 6 6l1.3-1.3a2 2 0 0 1 2.1-.5c.9.3 1.8.6 2.8.7a2 2 0 0 1 1.8 2.1z"/></svg>
    +1 555 014 2780
  </div>
  <div class="abs portrait-ring">
    <div class="abs portrait" role="img" aria-label="Portrait photograph of Lukas Brandstetter in a dark suit"></div>
  </div>
  <h1 class="abs hero-title">WE <em>AWAKEN</em> THE<br>TIGER IN <em>YOU</em>!</h1>
  <div class="abs btn hero-btn">Get Started</div>
  <div class="abs scroll-marks"><span></span><span></span><span></span><span class="on"></span></div>
</header>

<!-- About -->
<section>
  <h2 class="abs section-title" style="top:745px">About Me</h2>
  <div class="abs about-text">
    <p>Nemo enim ipsam voluptaem quia voluptas sit aspernatur aut odit aut fugit, sed quia consequuntur magni dolores eos qui ratione voluptatem sequi nesciunt. Neque porro quisquam est, qui dolorem ipsum quia dolor.</p>
    <p>Ut enim ad minima veniam, quis nostrum exercitationem ullam corporis suscipit laboriosam, nisi ut aliquid ex ea commodi consequatur? Quis autem vel eum iure reprehenderit qui in ea voluptate velit esse quam nihil molestiae consequatur, vel illum qui dolorem eum fugiat quo voluptas nulla pariatur.</p>
  </div>
  <div class="abs btn about-btn">Read More</div>
</section>

<!-- Services -->
<section class="abs services">
  <h2 class="abs section-title" style="top:76px">Our Services</h2>
  <div class="abs rule" style="left:539px;top:143px;width:130px"></div>

  <div class="abs svc svc-light" style="left:92px;top:198px">
    <svg class="abs" style="left:0;top:0" width="320" height="320" viewBox="0 0 320 320" fill="none">
      <circle cx="160" cy="160" r="140" stroke="var(--ring)" stroke-width="8" stroke-dasharray="620 260" transform="rotate(-50 160 160)"/>
      <circle cx="160" cy="160" r="153" stroke="var(--white)" stroke-width="3" stroke-dasharray="260 700" transform="rotate(100 160 160)"/>
    </svg>
    <div class="abs svc-body"><h3>Honest</h3><p>Excepteur sint occaecat cupidatat non proident, eculpa lorem Read More...</p></div>
  </div>

  <div class="abs svc svc-dark" style="left:434px;top:198px">
    <svg class="abs" style="left:0;top:0" width="320" height="320" viewBox="0 0 320 320" fill="none">
      <circle cx="160" cy="160" r="140" stroke="var(--white)" stroke-width="8" stroke-dasharray="620 260" transform="rotate(-50 160 160)"/>
      <circle cx="160" cy="160" r="153" stroke="var(--white)" stroke-width="3" stroke-dasharray="260 700" transform="rotate(100 160 160)"/>
      <circle cx="160" cy="160" r="128" stroke="var(--white)" stroke-width="3"/>
    </svg>
    <div class="abs svc-body"><h3>Human</h3><p>Duis aute irure dolor in reprehenderit in voluptate Read More....</p></div>
  </div>

  <div class="abs svc svc-light" style="left:775px;top:198px">
    <svg class="abs" style="left:0;top:0" width="320" height="320" viewBox="0 0 320 320" fill="none">
      <circle cx="160" cy="160" r="140" stroke="var(--ring)" stroke-width="8" stroke-dasharray="620 260" transform="rotate(-50 160 160)"/>
      <circle cx="160" cy="160" r="153" stroke="var(--white)" stroke-width="3" stroke-dasharray="260 700" transform="rotate(100 160 160)"/>
    </svg>
    <div class="abs svc-body"><h3>Trusting</h3><p>Quis autem vel eum iure reprehenderit qui in ea voluptate lor Read More..</p></div>
  </div>
</section>

<!-- Testimonials -->
<section>
  <h2 class="abs section-title" style="top:1945px">What Customer Says</h2>
  <div class="abs rule" style="left:539px;top:2011px;width:130px"></div>
  <div class="abs quote-badge">
    <svg width="64" height="64" viewBox="0 0 64 64"><path fill="#fff" d="M20 27h9v10h-5c0 3 1 5 4 6v3c-6-1-8-5-8-10zM34 27h9v10h-5c0 3 1 5 4 6v3c-6-1-8-5-8-10z" transform="translate(0,-4)"/></svg>
  </div>
  <div class="abs t-name">Daniel Weber<span class="stars">★★★★★</span></div>
  <p class="abs t-text">Lorem ipsum dolor sit amet, consectetur adipiscing elit, sed do eiusmod tempor incididunt ut labore et dolore magna aliqua. Ut enim ad minim veniam, quis nostrud exercitation ullamco laboris nisi ut aliquip ex ea commodo consequat fugiat nulla pariatur.</p>
  <p class="abs t-thanks">Thanks, <b>Lukas Brandstetter</b></p>
  <p class="abs t-side" style="left:-130px;top:2178px">r aut odit aut fugit, sed neque porro quisquam oluptatem. Ut enim ad di consequatur</p>
  <div class="abs t-side-name" style="left:1097px;top:2128px">Clara</div>
  <p class="abs t-side" style="left:1015px;top:2178px;text-align:left">Nemo enim ipsam vol quia dolores eos qui est, qui dolorem ipsu minima venia</p>
  <div class="abs dots"><span></span><span class="on"></span><span></span></div>
</section>

<!-- Video -->
<section class="abs video-band"></section>
<div class="abs video-frame">
  <div class="abs video-still" role="img" aria-label="Photograph of a smiling woman working on a laptop in a living room"></div>
  <svg class="abs play" viewBox="0 0 62 62"><circle cx="31" cy="31" r="29" fill="#fff" stroke="var(--red)" stroke-width="4"/><circle cx="31" cy="31" r="22" fill="var(--red)"/><path d="M26 21l15 10-15 10z" fill="#fff"/></svg>
  <div class="abs video-brand"><div class="brand"><span class="brand-dot"></span><span class="brand-name" style="font-size:19px">Lukas Brandstetter</span></div></div>
</div>

<!-- News -->
<section>
  <h2 class="abs section-title" style="top:3186px">Latest News</h2>

  <article class="abs card" style="left:115px">
    <div class="abs card-img" role="img" aria-label="Photograph of an athlete in a dark gym" style="background:linear-gradient(180deg,#3a3a3a,#161616)"></div>
    <div class="abs card-stars">★★★★★<span>(121)</span></div>
    <h3>Aliquam Quaerat Volupta</h3>
    <div class="abs card-date">Jan 08,2022</div>
    <p class="abs card-text">Ut enim ad minima veniam, quis nostrum etatioem ullam corpors suscipit</p>
    <div class="abs card-foot"><span class="avatar"></span>Lorem Ipsum</div>
  </article>

  <article class="abs card" style="left:449px">
    <div class="abs card-img" role="img" aria-label="Photograph of a woman working at a computer in an office" style="background:linear-gradient(160deg,#7f95a8,#3c4a58)"></div>
    <div class="abs card-stars">★★★★★<span>(134)</span></div>
    <h3>Nemo enim ipsam</h3>
    <div class="abs card-date">Jan 22,2022</div>
    <p class="abs card-text">Excepteur sint ocecat cupitat non proidnt, sunt inculpa qu officia deserunt.</p>
    <div class="abs card-foot"><span class="avatar"></span>Ullam Doe</div>
  </article>

  <article class="abs card" style="left:783px">
    <div class="abs card-img" role="img" aria-label="Photograph of a person using a phone beside a monitor" style="background:linear-gradient(160deg,#5a6f86,#243447)"></div>
    <div class="abs card-stars">★★★★★<span>(121)</span></div>
    <h3>Nostrum Exercitationem</h3>
    <div class="abs card-date">Jan 08,2022</div>
    <p class="abs card-text">Quis autem vel eum iure rerit qui in ea voluptate velit esse quam nihil molestiae.</p>
    <div class="abs card-foot"><span class="avatar"></span>Lorem Ipsum</div>
  </article>

  <div class="abs btn news-btn">Read More</div>
</section>

<!-- Footer -->
<footer class="abs footer">
  <div class="abs brand" style="left:115px;top:110px">
    <span class="brand-dot" style="width:18px;height:18px"></span>
    <div><div class="brand-name" style="font-size:12px">Lukas Brandstetter</div></div>
  </div>
  <p class="abs f-about">Nemo enim ipsam volutem quia voluptas sit asprnar aut odit aut fugit, sed quia consequunr magni dolores eos qui ratione voluptatem sequi nesciunt, Neque poro quisquam est, qui dolem.</p>

  <div class="abs f-head" style="left:383px">Contact Me</div>
  <div class="f-list">
    <div class="f-item" style="left:383px;top:160px"><svg width="14" height="14" viewBox="0 0 24 24" fill="none" stroke="#fff" stroke-width="2"><path d="M12 22s7-7 7-12a7 7 0 0 0-14 0c0 5 7 12 7 12z"/><circle cx="12" cy="10" r="2.5"/></svg><span>12 Linden Street<br>&nbsp;Brandstetter</span></div>
    <div class="f-item" style="left:383px;top:227px"><svg width="14" height="14" viewBox="0 0 24 24" fill="none" stroke="#fff" stroke-width="2"><path d="M22 16.9v3a2 2 0 0 1-2.2 2A19.8 19.8 0 0 1 2.1 4.2 2 2 0 0 1 4.1 2h3a2 2 0 0 1 2 1.7l.7 2.8-1.8 3.4a16 16 0 0 0 6 6l3.4-1.8 2.8.7a2 2 0 0 1 1.8 2.1z"/></svg><span>+1 555 014 2780</span></div>
    <div class="f-item" style="left:383px;top:269px"><svg width="14" height="14" viewBox="0 0 24 24" fill="none" stroke="#fff" stroke-width="2"><rect x="3" y="5" width="18" height="14" rx="1"/><path d="M3 6l9 7 9-7"/></svg><span>info@lbcoach.com</span></div>
    <div class="f-item" style="left:383px;top:311px"><svg width="14" height="14" viewBox="0 0 24 24" fill="none" stroke="#fff" stroke-width="2"><circle cx="12" cy="12" r="9"/><path d="M3 12h18M12 3c3 3 3 15 0 18M12 3c-3 3-3 15 0 18"/></svg><span>www.lbcoach.com</span></div>
  </div>

  <div class="abs f-head" style="left:609px">Quick Links</div>
  <span class="f-link" style="left:610px;top:156px">Home</span>
  <span class="f-link" style="left:727px;top:156px">Recent News</span>
  <span class="f-link" style="left:610px;top:193px">About Me</span>
  <span class="f-link" style="left:727px;top:193px">Testimonials</span>
  <span class="f-link" style="left:610px;top:230px">Services</span>
  <span class="f-link" style="left:727px;top:230px">Contact</span>
  <span class="f-link" style="left:610px;top:270px;font-weight:700;color:#fff">Follow Me</span>
  <span class="abs social" style="left:614px;top:302px"></span>
  <span class="abs social" style="left:661px;top:302px"></span>
  <span class="abs social" style="left:709px;top:302px"></span>
  <span class="abs social" style="left:757px;top:302px"></span>

  <div class="abs f-head" style="left:878px">Newsletter</div>
  <div class="abs news-input">Enter Your Mail</div>
  <div class="abs news-submit">SUBMIT</div>

  <div class="abs f-rule"></div>
  <div class="abs copyright">Copyrights@2022.All Rights Reserved</div>
</footer>

</body>
</html>
```